Packaging design for a reclosable bag for our product

We have a logo, and we need to put it on packaging for our product and while we want the look to be simple, we want it to follow good design principles and also contain spaces for other product descriptions.

There will be 5 sizes at launch so I'd like 5 variations, one for each size.

I've included a few mockups of the type of bag that I made but they are all just rough ideas that I had.

I want the brand to look scientific and methodical and even a bit quirky, as in "wow this is a serious product but also a bit unusual."

```html
<!DOCTYPE html>
<html lang="en">
<head>
<meta charset="utf-8">
<title>KQ4 Bias Lighting – 5m Pouch</title>
<link rel="stylesheet" href="https://fonts.googleapis.com/css2?family=Montserrat:wght@600;700&display=swap">
<style>
  :root {
    --backdrop: #808080;
    --pouch: #050505;
    --seal: #1c1c1c;
    --ink: #f2f2f2;
  }
  * { margin: 0; padding: 0; box-sizing: border-box; }
  html, body { width: 1200px; height: 789px; overflow: hidden; }
  body {
    background: var(--backdrop);
    font-family: "Montserrat", Arial, sans-serif;
    color: var(--ink);
    position: relative;
  }
  .pouch {
    position: absolute;
    left: 325px;
    top: 45px;
    width: 550px;
    height: 700px;
    background: var(--pouch);
    box-shadow: 0 8px 18px rgba(0,0,0,0.35);
  }
  .pouch-seal {
    position: absolute;
    inset: 0;
    width: 100%;
    height: 100%;
  }
  .brand-name {
    position: absolute;
    left: 73px;
    top: 152px;
    font-weight: 700;
    font-size: 68px;
    line-height: 1;
    letter-spacing: -2px;
  }
  .product-title {
    position: absolute;
    left: 76px;
    top: 292px;
    font-weight: 700;
    font-size: 29px;
    line-height: 34px;
  }
  .title-rule {
    position: absolute;
    left: 77px;
    top: 386px;
    width: 77px;
    height: 2px;
    background: var(--ink);
  }
  .product-size {
    position: absolute;
    left: 77px;
    top: 398px;
    font-weight: 700;
    font-size: 29px;
    line-height: 34px;
  }
  .product-spec {
    position: absolute;
    left: 77px;
    top: 488px;
    font-weight: 600;
    font-size: 16px;
    line-height: 29px;
    letter-spacing: 0.2px;
  }
</style>
</head>
<body>
  <div class="pouch">
    <svg class="pouch-seal" viewBox="0 0 550 700" aria-hidden="true">
      <g fill="none" stroke="var(--seal)" stroke-width="1.5">
        <rect x="8" y="8" width="534" height="684"/>
        <rect x="14" y="14" width="522" height="672"/>
        <rect x="20" y="20" width="510" height="660"/>
        <rect x="26" y="26" width="498" height="648"/>
      </g>
    </svg>

    <div class="brand-name">KQ4</div>

    <h1 class="product-title">BIAS<br>LIGHTING</h1>
    <div class="title-rule"></div>
    <div class="product-size">5m</div>

    <p class="product-spec">6500K WHITE BIAS LIGHTING<br>SIMULATED D95 CRI 90+</p>
  </div>
</body>
</html>
```